Website redesign

Redesign the Website

http://www.lindmark-schoefer.de/

Task

- make 1 Layout for the Website
- Colors: white, yellow, brown
- Text: Take from Page - ore rather Use Latin - Lore Ipsum ...
- pimp design and overall look
- enhance overview for better orientation
- more freindly / sympatic overall look.
- Better integrate Mingleroo Button aso.
- send Layout as layered PSD

```html
<!DOCTYPE html>
<html lang="de">
<head>
<meta charset="utf-8">
<title>Lindmark Schöfer – Trauringe</title>
<link href="https://fonts.googleapis.com/css2?family=Quicksand:wght@400;500;600&family=Open+Sans:wght@400;600&display=swap" rel="stylesheet">
<style>
:root{
  --gold:#f2b51c;
  --gold-soft:#fbe9a6;
  --cream:#fdf6dc;
  --brown:#5a3a1c;
  --brown-dark:#3b2614;
  --text:#4a4a4a;
  --muted:#9a9a9a;
  --line:#e4e4e4;
  --footer:#f3f1ec;
  --white:#ffffff;
}
*{margin:0;padding:0;box-sizing:border-box}
html,body{width:1200px;height:2232px;overflow:hidden;background:var(--white)}
body{font-family:"Open Sans",sans-serif;color:var(--text);font-size:12px;position:relative}
.abs{position:absolute}
.header{left:0;top:0;width:1200px;height:120px;background:var(--white)}
.logo{left:100px;top:40px;display:flex;align-items:center;gap:10px;font-family:"Quicksand",sans-serif;font-weight:600;font-size:22px;color:var(--brown)}
.logo i{width:22px;height:22px;border-radius:50%;background:var(--gold);display:block}
.nav{right:100px;top:0;display:flex;height:80px}
.nav a{display:flex;align-items:center;padding:0 26px;font-size:12px;letter-spacing:.5px;color:var(--text);text-decoration:none;font-weight:600}
.nav a.active{background:var(--gold);color:var(--white)}
.hero{left:0;top:120px;width:1200px;height:420px;background:linear-gradient(100deg,#f4efe9 0%,#e9ddd4 45%,#e6c9b8 70%,#efe6d6 100%)}
.hero-title{left:100px;top:230px;font-family:"Quicksand",sans-serif;font-weight:400;font-size:38px;line-height:52px;color:var(--text)}
.hero-title span{display:block;padding-left:110px}
.dots{left:570px;top:500px;display:flex;gap:8px}
.dots i{width:10px;height:10px;border-radius:50%;background:#c9c0b8;display:block}
.dots i:first-child{background:var(--gold)}
.partner{left:520px;top:565px;width:160px;height:70px;display:flex;flex-direction:column;align-items:center;justify-content:center;border-top:1px solid var(--line);border-bottom:1px solid var(--line);font-family:"Quicksand",sans-serif;font-size:22px;font-weight:500;color:var(--brown)}
.section-title{left:0;width:1200px;text-align:center;font-family:"Quicksand",sans-serif;font-size:24px;color:var(--text)}
.section-title:before,.section-title:after{content:"";display:inline-block;width:380px;height:1px;background:var(--line);vertical-align:middle;margin:0 24px}
.row{left:140px;width:920px;display:flex;justify-content:space-between}
.product{width:150px;text-align:center;font-size:10px;line-height:14px;color:var(--muted)}
.thumb{width:150px;height:130px;margin-bottom:12px}
.t-gold{background:radial-gradient(circle at 50% 55%,#f6d77a 0,#e2b23c 35%,#fff 62%)}
.t-silver{background:radial-gradient(circle at 50% 55%,#e9e9e9 0,#b9b9b9 35%,#fff 62%)}
.t-mix{background:radial-gradient(circle at 50% 55%,#f0e3c4 0,#c9b48a 35%,#fff 62%)}
.t-rose{background:radial-gradient(circle at 50% 55%,#f0c3a8 0,#d69373 35%,#fff 62%)}
.arrow{width:20px;height:20px}
.btn-more{left:550px;width:100px;height:26px;border:1px solid var(--line);border-radius:13px;font-size:10px;color:var(--muted);display:flex;align-items:center;justify-content:center}
.banner{left:0;top:1385px;width:1200px;height:195px;background:linear-gradient(90deg,#fdf3c8,#fbe7a0 60%,#fdf3c8)}
.banner h2{position:absolute;left:100px;top:60px;font-family:"Quicksand",sans-serif;font-weight:500;font-size:32px;color:var(--brown)}
.btn-gold{background:var(--gold);color:var(--white);border-radius:16px;font-size:11px;font-weight:600;display:flex;align-items:center;justify-content:center}
.banner-rings{left:760px;top:1400px;width:220px;height:165px;background:radial-gradient(ellipse at center,#f0c54a 0,#e8b52c 30%,rgba(251,231,160,0) 65%)}
.feature{left:100px;top:1660px;width:480px;height:230px;border:1px solid var(--line);background:var(--white)}
.feature .img{position:absolute;left:0;top:0;width:230px;height:228px;background:radial-gradient(circle,#f3cc5f 0,#dba633 30%,#f6f1e6 65%)}
.feature h3{position:absolute;left:248px;top:30px;font-family:"Quicksand",sans-serif;font-size:16px;line-height:22px;font-weight:600;color:var(--gold);white-space:nowrap}
.feature p{position:absolute;left:248px;top:66px;width:215px;font-size:10px;line-height:15px;color:var(--muted)}
.video{left:620px;top:1660px;width:480px;height:230px;background:linear-gradient(160deg,#2d2a28,#544a40 60%,#8a7660)}
.video .bar{position:absolute;left:0;top:0;width:480px;height:28px;background:rgba(0,0,0,.45);color:#ddd;font-size:11px;padding:7px 12px}
.cta{left:100px;top:1940px;width:1000px;display:flex;align-items:center;justify-content:space-between;border-top:1px solid var(--line);border-bottom:1px solid var(--line);padding:18px 0}
.cta p{font-family:"Quicksand",sans-serif;font-size:21px;color:var(--text)}
.footer{left:0;top:2020px;width:1200px;height:160px;background:var(--footer)}
.fcol{top:2050px;font-size:10px;line-height:16px;color:var(--muted)}
.fcol b{color:var(--text);font-weight:600}
.bottom{left:0;top:2180px;width:1200px;height:52px;background:var(--brown-dark);color:#cdbfae;font-size:10px}
.bottom .copy{position:absolute;left:100px;top:19px}
.bottom .like{position:absolute;right:100px;top:15px;display:flex;align-items:center;gap:8px}
.bottom .like span.btn{background:#6d5a47;color:var(--white);padding:3px 8px;border-radius:3px;font-weight:600}
</style>
</head>
<body>
<header class="abs header">
  <div class="abs logo"><i></i>Lindmark Schöfer</div>
  <nav class="abs nav">
    <a class="active" href="#">TRAURINGE</a>
    <a href="#">SOLITÄRRINGE</a>
    <a href="#">EHERINGE</a>
    <a href="#">BOUTIQUE</a>
    <a href="#">INFORMATIONEN</a>
    <a href="#">KONTAKT</a>
  </nav>
</header>

<section class="abs hero" role="img" aria-label="Foto: Hände eines Brautpaares mit Trauringen und Blumenstrauß"></section>
<h1 class="abs hero-title">Die schönsten Trauringe…<span>…ein Leben lang</span></h1>
<div class="abs dots"><i></i><i></i><i></i></div>

<div class="abs partner">Halvern</div>

<h2 class="abs section-title" style="top:670px">Trauringe</h2>
<svg class="abs arrow" style="left:100px;top:800px" viewBox="0 0 20 20"><path d="M13 4 7 10l6 6" fill="none" stroke="#999" stroke-width="2"/></svg>
<svg class="abs arrow" style="left:1080px;top:800px" viewBox="0 0 20 20"><path d="M7 4l6 6-6 6" fill="none" stroke="#999" stroke-width="2"/></svg>
<div class="abs row" style="top:725px">
  <div class="product"><div class="thumb t-gold" role="img" aria-label="Foto: Trauringpaar Gelbgold"></div>Trauring Modell 01<br>585 Gelbgold 4,5 mm</div>
  <div class="product"><div class="thumb t-mix" role="img" aria-label="Foto: Trauringpaar Bicolor"></div>Trauring Modell 02<br>585 Bicolor 5,0 mm</div>
  <div class="product"><div class="thumb t-silver" role="img" aria-label="Foto: Trauringpaar Weißgold"></div>Trauring Modell 03<br>585 Weißgold 4,0 mm</div>
  <div class="product"><div class="thumb t-rose" role="img" aria-label="Foto: Trauringpaar Rotgold"></div>Trauring Modell 04<br>585 Rotgold 5,5 mm</div>
  <div class="product"><div class="thumb t-silver" role="img" aria-label="Foto: Trauringpaar Platin"></div>Trauring Modell 05<br>950 Platin 4,5 mm</div>
</div>
<div class="abs btn-more" style="top:950px">mehr sehen</div>

<h2 class="abs section-title" style="top:1005px">Solitärringe</h2>
<svg class="abs arrow" style="left:100px;top:1135px" viewBox="0 0 20 20"><path d="M13 4 7 10l6 6" fill="none" stroke="#999" stroke-width="2"/></svg>
<svg class="abs arrow" style="left:1080px;top:1135px" viewBox="0 0 20 20"><path d="M7 4l6 6-6 6" fill="none" stroke="#999" stroke-width="2"/></svg>
<div class="abs row" style="top:1060px">
  <div class="product"><div class="thumb t-gold" role="img" aria-label="Foto: Solitärring Gelbgold"></div>Solitär Modell 11<br>585 Gelbgold 0,10 ct</div>
  <div class="product"><div class="thumb t-mix" role="img" aria-label="Foto: Solitärring Bicolor"></div>Solitär Modell 12<br>585 Bicolor 0,15 ct</div>
  <div class="product"><div class="thumb t-silver" role="img" aria-label="Foto: Solitärring Weißgold"></div>Solitär Modell 13<br>585 Weißgold 0,20 ct</div>
  <div class="product"><div class="thumb t-rose" role="img" aria-label="Foto: Solitärring Rotgold"></div>Solitär Modell 14<br>585 Rotgold 0,10 ct</div>
  <div class="product"><div class="thumb t-mix" role="img" aria-label="Foto: Solitärring Gold"></div>Solitär Modell 15<br>750 Gelbgold 0,25 ct</div>
</div>
<div class="abs btn-more" style="top:1295px">mehr sehen</div>

<section class="abs banner">
  <h2>Veralto: Brautschmuck aus Titan</h2>
  <div class="abs btn-gold" style="left:100px;top:118px;width:110px;height:26px">mehr lesen</div>
</section>
<div class="abs banner-rings" role="img" aria-label="Foto: zwei goldene Trauringe"></div>

<article class="abs feature">
  <div class="img" role="img" aria-label="Foto: Trauringpaar Gelbgold"></div>
  <h3>Trauringe selbst gestalten</h3>
  <p>Gestalten Sie Ihre Trauringe ganz nach Ihren Wünschen. Wählen Sie Material, Breite, Profil und Steinbesatz und sehen Sie Ihr Ergebnis sofort. Gerne beraten wir Sie persönlich in unserem Geschäft und begleiten Sie bei jedem Schritt bis zum fertigen Ring.</p>
  <div class="abs btn-gold" style="left:248px;top:182px;width:100px;height:24px">jetzt starten</div>
</article>
<div class="abs video" role="img" aria-label="Video: Vorstellung des Geschäfts">
  <div class="bar">Lindmark Schöfer – Unser Geschäft</div>
  <svg class="abs" style="left:210px;top:85px" width="60" height="60" viewBox="0 0 60 60"><circle cx="30" cy="30" r="28" fill="rgba(0,0,0,.55)"/><path d="M24 18l18 12-18 12z" fill="#fff"/></svg>
</div>

<div class="abs cta">
  <p>Möchten Sie einen Termin vereinbaren? Haben Sie Fragen zu Lindmark Schöfer?</p>
  <div class="btn-gold" style="width:110px;height:28px">Kontakt</div>
</div>

<footer class="abs footer"></footer>
<div class="abs logo" style="top:2055px;font-size:17px"><i style="width:18px;height:18px"></i>Lindmark Schöfer</div>
<div class="abs fcol" style="left:330px"><b>Lindmark Schöfer GmbH</b><br>Lindenstraße 12a<br>00000 Musterstadt</div>
<div class="abs fcol" style="left:490px"><b>Öffnungszeiten</b><br>Di–Fr 10:00–18:00<br>+49 0 000 482 190<br>info@lindmark-schoefer.de</div>
<div class="abs fcol" style="left:690px"><b>Trauringe</b><br>Gelbgold<br>Weißgold<br>Platin</div>
<div class="abs fcol" style="left:820px"><b>Service</b><br>Beratung<br>Gravur<br>Anfahrt</div>
<div class="abs fcol" style="left:960px"><b>Rechtliches</b><br>Impressum<br>Datenschutz<br>AGB</div>

<div class="abs bottom">
  <span class="copy">Copyright © 2015 lindmark-schoefer.de · Alle Rechte vorbehalten</span>
  <span class="like">Like us on Mingleroo <span class="btn">Gefällt mir</span></span>
</div>
</body>
</html>
```